Guaranteed Job - Sleek Sexy Business Card UV Spot

Im looking for a sleek and sexy business card, that resembles elite or VIP status status.
our business is corinvale.example
you can view our products on there, but our main audience for handing out our cards will be for people in the hospitality industry, so it will need to impress high management and CEO of hotels and restaurants, bars, clubs etc...
the card features will have UV spot on both sides, 400gsm stock. standard size.
Artwork should be 86 x 54mm + 2mm bleed = 90 x 58mm
it should have a nice "unique" uv spot pattern that highlights the card, not a repeated pattern, theres no originality there, and it will be disregarded.
The written material will be:
Corin Vale Hospitality College (logo)
Tobin Marsh
Director
Phone: 1300 615 737
Mobile: 0455 817 296
Email: info@corinvale.example
website: www.corinvale.example
I'm looking for originality here, i don't want just a simple stock card, want something that has a wow factor for people.
You will find the logo attached. you may invert the white to black words to suit the background as you please.
thank you and good luck
As a side note, ive received a lot of proposals, im too busy to give feedback to each and every one, so if i havent provided feedback for your design within 24 hours, then consider it not acceptable, and you could resubmit another design.
So far i have not seen any design that stood out for me, they all seem pretty generic. there nothing thats unique, i would figure for the amount that im offering, that people would put some more effort and creativity into the design.
so far over 200 designs submitted, and nothing i have seen looks very original, everything looks like a different variation of the same stuff, i said it very clearly i wanted something unique, the only thing that has come close to it so far is this one
Reason: Ive received alot of design concepts and i have reviewed everyone, but i havent had time to give feedback to every single one, only the ones that have interested me, if i havent responded, its because i havent found it good enough.
so far only a few design have been on par with what ive been looking for, an attractive eye popping design.
heres a few of them,
http://files.pixelbazaar.example/design_img/51736/62418/62418_2840915_51736_image.jpg
http://files.pixelbazaar.example/design_img/51736/68254/68254_2841377_51736_image.jpg
theyre, both unique and original, and eye catching, the only thing theyre missing is the sexyness.
if you still think you have some creativity left in your minds, then throw it on here.
Reason: Sorry guys for the delay, I was in a serious accident and out of commission for the past few months, I'm just slowly recovering now, please bare with me as i try to attend to this project, it may take me awhile as I have other projects that are on standby, I'm not 100% at the moment, so im extending the deadline for 2 weeks right now. Thanks for your patience.
Hospitality

```html
<!DOCTYPE html>
<html lang="en">
<head>
<meta charset="utf-8">
<title>Corin Vale Hospitality College – Business Card</title>
<link rel="stylesheet" href="https://fonts.googleapis.com/css2?family=Montserrat:wght@500;600&family=Ubuntu:wght@400&display=swap">
<style>
  :root {
    --page-bg: #e6e7e9;
    --card-bg: #ffffff;
    --ink: #1c2430;
    --accent-blue: #5b86bd;
    --icon-ink: #20262e;
    --art-magenta: #e2358f;
    --art-red: #e8333d;
    --art-yellow: #e9d43a;
    --art-blue: #2f74c9;
    --art-sky: #49b7e6;
    --art-violet: #b99ad6;
  }
  * { margin: 0; padding: 0; box-sizing: border-box; }
  html, body { width: 1200px; height: 861px; overflow: hidden; }
  body {
    background: var(--page-bg);
    display: flex;
    align-items: center;
    justify-content: center;
  }
  .business-card {
    position: relative;
    width: 860px;
    height: 540px;
    background: var(--card-bg);
    border-radius: 24px;
    overflow: hidden;
    box-shadow: 0 10px 30px rgba(0, 0, 0, 0.15);
  }
  .card-art {
    position: absolute;
    inset: 0;
    width: 100%;
    height: 100%;
  }
  .brand {
    position: absolute;
    left: 60px;
    top: 62px;
    display: flex;
    align-items: center;
    gap: 16px;
  }
  .brand-dot {
    width: 22px;
    height: 22px;
    border-radius: 50%;
    background: var(--accent-blue);
  }
  .brand-name {
    font-family: "Montserrat", sans-serif;
    font-weight: 600;
    font-size: 26px;
    line-height: 1.12;
    letter-spacing: 1px;
    color: var(--ink);
    text-transform: uppercase;
  }
  .brand-name small {
    display: block;
    font-size: 13px;
    letter-spacing: 1.4px;
  }
  .person {
    position: absolute;
    left: 60px;
    top: 215px;
  }
  .person-name {
    font-family: "Montserrat", sans-serif;
    font-weight: 500;
    font-size: 60px;
    line-height: 1;
    color: var(--ink);
    letter-spacing: 0.5px;
  }
  .person-title {
    font-family: "Montserrat", sans-serif;
    font-weight: 500;
    font-size: 32px;
    color: var(--accent-blue);
    margin-top: 4px;
    letter-spacing: 0.5px;
  }
  .contacts {
    position: absolute;
    left: 60px;
    top: 355px;
    list-style: none;
  }
  .contact-line {
    display: flex;
    align-items: center;
    gap: 14px;
    font-family: "Ubuntu", sans-serif;
    font-size: 26px;
    color: var(--ink);
    height: 38px;
  }
  .contact-icon { width: 24px; height: 24px; flex: none; }
</style>
</head>
<body>
  <main class="business-card">
    <svg class="card-art" viewBox="0 0 860 540" role="img" aria-label="Colourful abstract artwork of overlapping bubbles and diagonal stripes in magenta, red, yellow and blue">
      <defs>
        <linearGradient id="art-fill" x1="0" y1="0.3" x2="1" y2="0.7">
          <stop offset="0" stop-color="var(--art-violet)" stop-opacity="0.55"/>
          <stop offset="0.3" stop-color="var(--art-magenta)"/>
          <stop offset="0.5" stop-color="var(--art-red)"/>
          <stop offset="0.68" stop-color="var(--art-yellow)"/>
          <stop offset="0.85" stop-color="var(--art-blue)"/>
          <stop offset="1" stop-color="var(--art-sky)"/>
        </linearGradient>
        <linearGradient id="corner-fill" x1="0" y1="0" x2="1" y2="1">
          <stop offset="0" stop-color="var(--art-magenta)"/>
          <stop offset="1" stop-color="var(--art-violet)"/>
        </linearGradient>
        <radialGradient id="art-fade" cx="0.75" cy="0.6" r="0.6">
          <stop offset="0.6" stop-color="#fff" stop-opacity="0"/>
          <stop offset="1" stop-color="#fff" stop-opacity="0.5"/>
        </radialGradient>
      </defs>
      <polygon points="770,0 860,0 860,120" fill="url(#corner-fill)" opacity="0.8"/>
      <path d="M420 540 C430 420 480 330 560 260 C640 200 730 170 860 150 L860 540 Z" fill="url(#art-fill)"/>
      <path d="M420 540 C430 420 480 330 560 260 C640 200 730 170 860 150 L860 540 Z" fill="url(#art-fade)"/>
    </svg>

    <header class="brand">
      <span class="brand-dot"></span>
      <div class="brand-name">Corin Vale<small>Hospitality College</small></div>
    </header>

    <section class="person">
      <h1 class="person-name">Tobin Marsh</h1>
      <p class="person-title">Director</p>
    </section>

    <ul class="contacts">
      <li class="contact-line">
        <svg class="contact-icon" viewBox="0 0 24 24" aria-hidden="true"><circle cx="12" cy="12" r="10.5" fill="none" stroke="var(--icon-ink)" stroke-width="2.2"/><path d="M8 16 L16 8" stroke="var(--icon-ink)" stroke-width="3" stroke-linecap="round"/></svg>
        1300 615 737
      </li>
      <li class="contact-line">
        <svg class="contact-icon" viewBox="0 0 24 24" aria-hidden="true"><circle cx="12" cy="12" r="10.5" fill="none" stroke="var(--icon-ink)" stroke-width="2.2"/><rect x="9" y="6" width="6" height="12" rx="1.2" fill="var(--icon-ink)"/></svg>
        0455 817 296
      </li>
      <li class="contact-line">
        <svg class="contact-icon" viewBox="0 0 24 24" aria-hidden="true"><circle cx="12" cy="12" r="10.5" fill="none" stroke="var(--icon-ink)" stroke-width="2.2"/><rect x="6.5" y="8.5" width="11" height="7.5" fill="var(--icon-ink)"/><path d="M6.5 8.5 L12 13 L17.5 8.5" fill="none" stroke="#fff" stroke-width="1.2"/></svg>
        info@corinvale.example
      </li>
      <li class="contact-line">
        <svg class="contact-icon" viewBox="0 0 24 24" aria-hidden="true"><circle cx="12" cy="12" r="10.5" fill="none" stroke="var(--icon-ink)" stroke-width="2.2"/><rect x="6.5" y="7.5" width="11" height="8" rx="1" fill="none" stroke="var(--icon-ink)" stroke-width="1.8"/><rect x="9.5" y="15.5" width="5" height="1.8" fill="var(--icon-ink)"/></svg>
        www.corinvale.example
      </li>
    </ul>
  </main>
</body>
</html>
```